Timid Kitten Clinic Business Card Design

I need a business card designed for my cat only veterinary clinic. I will upload the logo that I would like included on the card. Please include:
Business Name: The Timid Kitten Clinic
Address: 4827 W. 39th Ln, Scottsdale, AZ 85317
Phone #: 480-555-6314
Website URL: www.timidkittenvet.example
And the Doctors Name: Marla Quint, DVM

```html
<!DOCTYPE html>
<html lang="en">
<head>
<meta charset="utf-8">
<title>The Timid Kitten Clinic – Business Card</title>
<link rel="stylesheet" href="https://fonts.googleapis.com/css2?family=Quicksand:wght@500&family=Mulish:wght@400;700;800&display=swap">
<style>
  :root {
    --stage: #3a3b3e;
    --card-blue: #4a80b4;
    --card-white: #ffffff;
    --card-white-shade: #ececec;
    --ink: #333333;
    --accent-blue: #4a80b4;
    --mark-dark: #1c1a33;
    --rule: #3b3b3b;
    --frame-grey: #c9cacc;
  }
  * { box-sizing: border-box; margin: 0; padding: 0; }
  html, body { width: 1200px; height: 900px; overflow: hidden; }
  body {
    background: var(--stage);
    position: relative;
    font-family: "Mulish", sans-serif;
    color: var(--ink);
  }
  .card {
    position: absolute;
    width: 560px;
    height: 320px;
    border-radius: 2px;
    box-shadow: 0 10px 24px rgba(0,0,0,0.45);
    overflow: hidden;
  }

  /* Back side */
  .card-back {
    left: 320px; top: 70px;
    background: var(--card-blue);
  }
  .card-back .brand-mark {
    position: absolute;
    left: 208px; top: 58px;
    width: 144px; height: 132px;
    background: var(--mark-dark);
  }
  .card-back .brand-name {
    position: absolute;
    left: 0; right: 0; top: 198px;
    text-align: center;
    font-family: "Quicksand", sans-serif;
    font-weight: 500;
    font-size: 24px;
    line-height: 1.1;
    color: #ffffff;
  }

  /* Front side */
  .card-front {
    left: 320px; top: 470px;
    background: linear-gradient(180deg, var(--card-white) 0%, var(--card-white-shade) 100%);
  }
  .card-front .brand-mark {
    position: absolute;
    left: 40px; top: 38px;
    width: 140px; height: 132px;
    background: var(--mark-dark);
  }
  .card-front .brand-name {
    position: absolute;
    left: 40px; top: 176px;
    font-family: "Quicksand", sans-serif;
    font-weight: 500;
    font-size: 19px;
    line-height: 1.1;
    color: var(--ink);
  }
  .photo-frame {
    position: absolute;
    left: 210px; top: 0;
    width: 350px; height: 170px;
  }
  .doctor-name {
    position: absolute;
    left: 40px; top: 232px;
    font-weight: 800;
    font-size: 20px;
    color: var(--accent-blue);
  }
  .doctor-name .credential { font-size: 13px; font-weight: 700; }
  .address {
    position: absolute;
    left: 300px; top: 190px;
    font-size: 14px;
    line-height: 1.45;
    color: var(--ink);
  }
  .rule {
    position: absolute;
    height: 1px;
    background: var(--rule);
  }
  .rule-upper { left: 200px; top: 182px; width: 260px; }
  .rule-lower { left: 24px; top: 262px; width: 270px; }
  .contact-list {
    position: absolute;
    left: 40px; top: 270px;
    list-style: none;
    font-size: 13.5px;
    line-height: 22px;
  }
  .contact-list li { display: flex; align-items: center; gap: 8px; }
  .contact-list svg { width: 14px; height: 14px; flex: none; }
</style>
</head>
<body>

  <section class="card card-back" aria-label="Business card, back">
    <div class="brand-mark"></div>
    <p class="brand-name">The Timid Kitten<br>Clinic</p>
  </section>

  <section class="card card-front" aria-label="Business card, front">
    <div class="brand-mark"></div>
    <p class="brand-name">The Timid Kitten<br>Clinic</p>

    <svg class="photo-frame" viewBox="0 0 350 170" aria-hidden="false">
      <defs>
        <linearGradient id="photo-tone" x1="0" y1="0" x2="1" y2="1">
          <stop offset="0" stop-color="#dfe3e8"/>
          <stop offset="0.5" stop-color="#9a928c"/>
          <stop offset="1" stop-color="#e9e6e2"/>
        </linearGradient>
      </defs>
      <path d="M0 0 H350 V130 Q350 170 310 170 H60 Q30 170 18 140 L0 100 Z" fill="var(--frame-grey)"/>
      <path d="M8 0 V95 L24 135 Q34 158 60 158 H320 Q342 158 342 135 V0 Z"
            fill="url(#photo-tone)" role="img" aria-label="Photo of a grey and white cat resting its head"/>
      <path d="M4 0 V100 L20 140 Q30 163 58 163 H326" fill="none" stroke="#222" stroke-width="1"/>
    </svg>

    <div class="rule rule-upper"></div>
    <p class="address">4827 W. 39th Ln<br>Scottsdale, AZ 85317</p>
    <p class="doctor-name">Marla Quint, <span class="credential">DVM</span></p>
    <div class="rule rule-lower"></div>

    <ul class="contact-list">
      <li>
        <svg viewBox="0 0 16 16" aria-hidden="true">
          <path d="M2 5 Q8 1 14 5 L12.5 7 L10.5 6 V5 H5.5 V6 L3.5 7 Z" fill="var(--accent-blue)"/>
          <rect x="3.5" y="8" width="9" height="6" rx="1" fill="var(--accent-blue)"/>
        </svg>
        <span>480-555-6314</span>
      </li>
      <li>
        <svg viewBox="0 0 16 16" aria-hidden="true">
          <circle cx="7" cy="7" r="5.5" fill="none" stroke="var(--accent-blue)" stroke-width="1.6"/>
          <path d="M4 6 Q6 4 8 6 T10 8" fill="none" stroke="var(--accent-blue)" stroke-width="1.2"/>
          <line x1="11" y1="11" x2="15" y2="15" stroke="var(--accent-blue)" stroke-width="1.8"/>
        </svg>
        <span>www.timidkittenvet.example</span>
      </li>
    </ul>
  </section>

</body>
</html>
```